Jewelry Business card for general purpose. Elegant and simple

We are a jewelry group with 6 stores in Mexico and 30 years in business.

We need a BC that at leats includes the name, mail, phone number and physical location (street, municipality, and county; example "Paseo Olmeda 2140", "Avenida Sotillo", "Monterrey").
Optional: we are trying to reposition the brand with the association of life-events or moments and family. Such as: birth, marriage, graduation, birthdays. Christmast, mothers day and fathers day.

We are looking for something elegant but simple

Jewelry name: "Lunetti". Email: "lunettibrillo@correo-ejemplo.mx". Phone num "4172-3095".

Target Market(s)

General business card: from suppliers to clients. One segment outstand: couples gettineg married

Industry/Entity Type

Jewelry Store

Contact Information for Business Card

Loking for something simple but elegant.

Font styles to use
Decorative
Script

Requirements
Must have
• Must have name, address, and mail.
Nice to have
• It could have jewelry pictures/design. Maybe quotes. Or general words as background . currently we have a very simple card with one ring would like to see something different.
Should not have
• Include real people.

```html
<!DOCTYPE html>
<html lang="es">
<head>
<meta charset="utf-8">
<title>Joyería Lunetti – Tarjeta de presentación</title>
<link rel="stylesheet" href="https://fonts.googleapis.com/css2?family=Sofia&family=Open+Sans:wght@400&display=swap">
<style>
  :root {
    --backdrop: #ece8e1;
    --gold-light: #f3b73a;
    --gold: #e5a21c;
    --gold-deep: #c98a10;
    --band: #050505;
    --rule: #ffffff;
    --script-gold: #f0b22e;
    --text-light: #f4f4f4;
    --jewel-warm: #c99a3c;
    --jewel-cool: #cfcfcf;
  }
  * { margin: 0; padding: 0; box-sizing: border-box; }
  html, body {
    width: 1200px; height: 1022px; overflow: hidden;
    background: var(--backdrop);
  }
  .business-card {
    position: absolute; left: 150px; top: 231px;
    width: 900px; height: 560px; border-radius: 20px; overflow: hidden;
    background: linear-gradient(160deg, var(--gold-light) 0%, var(--gold) 55%, var(--gold-deep) 100%);
    box-shadow: 0 10px 30px rgba(0,0,0,0.18);
  }
  .rule {
    position: absolute; left: 300px; right: 0; height: 5px;
    background: var(--rule);
  }
  .rule--top { top: 158px; }
  .rule--bottom { top: 418px; }
  .info-band {
    position: absolute; left: 300px; right: 0; top: 175px; height: 232px;
    background: var(--band);
    padding: 26px 0 0 46px;
    color: var(--text-light);
    font-family: "Open Sans", sans-serif;
    font-size: 21px; line-height: 31px;
  }
  .store-name {
    font-family: "Sofia", cursive;
    font-weight: 400; font-size: 40px; line-height: 52px;
    color: var(--script-gold);
    margin-bottom: 12px;
  }
  .contact-line { display: flex; align-items: center; gap: 10px; }
  .contact-line svg { width: 16px; height: 16px; flex: none; }
  .jewel-photo {
    position: absolute; left: 40px; top: 200px; width: 330px; height: 210px;
    border-radius: 50%;
    background: radial-gradient(ellipse at 50% 45%, var(--jewel-cool) 0%, var(--jewel-warm) 55%, rgba(201,154,60,0) 75%);
  }
</style>
</head>
<body>
  <article class="business-card">
    <div class="rule rule--top"></div>
    <section class="info-band">
      <h1 class="store-name">Joyería Lunetti</h1>
      <p>Paseo Olmeda 2140,</p>
      <p>Avenida Sotillo, Monterrey</p>
      <p class="contact-line">
        <svg viewBox="0 0 16 16" aria-hidden="true"><path d="M4 1.5 6.5 4 5 6c1 2 3 4 5 5l2-1.5 2.5 2.5-2 2.5C7 14 2 9 1.5 3.5z" fill="var(--script-gold)"/></svg>
        4172-3095
      </p>
      <p class="contact-line">
        <svg viewBox="0 0 16 16" aria-hidden="true"><rect x="1.5" y="3.5" width="13" height="9" fill="none" stroke="var(--script-gold)" stroke-width="1.6"/><path d="M2 4l6 5 6-5" fill="none" stroke="var(--script-gold)" stroke-width="1.6"/></svg>
        lunettibrillo@correo-ejemplo.mx
      </p>
    </section>
    <div class="rule rule--bottom"></div>
    <div class="jewel-photo" role="img" aria-label="Fotografía de un brazalete de oro con piedras engastadas"></div>
  </article>
</body>
</html>
```